Solvane Holdings Inc. Business Card Design

My business is custom renovations and homes.I would need to have a new business logo created to go along with my company name. The business card should be of a modern style as this is the market I am focused on. I would need my contact information and website posted on the card. I would also like to list a few of the tasks I conduct on the card (such as: Renovations, Additions, Repairs, New Homes, Design, Consultations). On the reverse of the card I currently have just my logo and my motto, "Shaping Fresh Ground". However, I am open to completely changing everything as I am starting a new year and would like to excel further. Any new ideas and suggestions are always welcomed. Thank you.

Target Market(s)

Upscale residential and commercial renovations and builds

Industry/Entity Type

Business

Contact Information for Business Card

I would like the design to be able to be laser cut or burnt onto a wooden business card. I will be creating one option of cards for really loyal customers (wooden) and a second option for the everyday customer (paper).

Font styles to use
Other font styles liked:
• Calibri / anything of mordern taste

Colors
f37122
5c5c5c
474747
ffffff

Requirements
Must have
• I would like the colours of my business to be a sharp orange and grey. I believe this will symbolize a modern style. I am open to other suggestions if this is not suitable for the designers tastes. My contact info as follows:
• Dirk Malsworth
• President
• Solvane Holdings Inc.
• 555-239-7814
• dirk@solvaneholdings.example
• I would like my website (currently under construction) solvaneholdings.example on the card aswell.
Nice to have
• Along with a modern logo representing Solvane, I would like something on the card besides the logo and contact information. Perhaps a small background design. I feel it may be nice to have my services listed on the card (in smaller font on the bottom) Renovations, Additions, Repairs, Design, Consultations.
Should not have
• The business card should not have too many different colors. Should not have rounded corners.

```html
<!DOCTYPE html>
<html lang="en">
<head>
<meta charset="utf-8">
<title>Solvane Holdings Inc. Business Card</title>
<link rel="stylesheet" href="https://fonts.googleapis.com/css2?family=Lato:wght@400;700&family=Roboto:wght@400&display=swap">
<style>
  :root {
    --orange: #f37122;
    --card-dark: #333333;
    --card-light: #ffffff;
    --text-grey: #5c5c5c;
    --text-dark: #474747;
    --stage: #d6d6d6;
    --white: #ffffff;
  }
  * { margin: 0; padding: 0; box-sizing: border-box; }
  html, body { width: 1200px; height: 1000px; overflow: hidden; }
  body {
    background: var(--stage);
    position: relative;
    font-family: "Lato", sans-serif;
  }
  .card {
    position: absolute;
    left: 287px;
    width: 627px;
    box-shadow: 0 4px 12px rgba(0,0,0,0.25);
  }
  .card--front { top: 140px; height: 358px; background: var(--card-dark); }
  .card--back  { top: 531px; height: 359px; background: var(--card-light); }

  .brand-square {
    position: absolute;
    background: var(--orange);
  }
  .card--front .brand-square { left: 148px; top: 136px; width: 84px; height: 84px; }
  .card--back .brand-square  { left: 90px; top: 92px; width: 176px; height: 176px; }

  .divider { position: absolute; width: 2px; }
  .card--front .divider { left: 267px; top: 134px; height: 88px; background: var(--white); }
  .card--back .divider {
    left: 302px; top: 91px; height: 176px; width: 2px;
    background: linear-gradient(to bottom, rgba(243,113,34,0), var(--orange) 25%, var(--orange) 75%, rgba(243,113,34,0));
  }

  .company-name {
    position: absolute;
    left: 285px; top: 142px;
    color: var(--white);
    font-weight: 700;
    font-size: 27px;
    line-height: 36px;
    letter-spacing: 0.2px;
  }

  .services {
    position: absolute;
    left: 0; right: 0; top: 303px;
    text-align: center;
    font-family: "Roboto", sans-serif;
    font-size: 14.5px;
    color: var(--white);
    letter-spacing: 0.3px;
  }
  .services .sep { color: var(--orange); margin: 0 6px; }

  .contact {
    position: absolute;
    left: 327px; top: 88px;
    color: var(--text-grey);
    font-size: 14.5px;
    line-height: 18px;
  }
  .contact__name { color: var(--orange); font-weight: 700; font-size: 19px; line-height: 22px; }
  .contact__title { margin-bottom: 13px; }
  .contact__company { color: var(--orange); }
  .contact__address { margin-bottom: 13px; }
  .contact__row { display: flex; align-items: center; height: 20px; }
  .contact__row svg { width: 10px; height: 10px; margin-right: 10px; fill: var(--orange); }
</style>
</head>
<body>
  <section class="card card--front" aria-label="Card front">
    <div class="brand-square"></div>
    <div class="divider"></div>
    <div class="company-name">Solvane<br>Holdings Inc.</div>
    <div class="services">Renovations<span class="sep">|</span>Additions<span class="sep">|</span>Repairs<span class="sep">|</span>New Homes<span class="sep">|</span>Consultations</div>
  </section>

  <section class="card card--back" aria-label="Card back">
    <div class="brand-square"></div>
    <div class="divider"></div>
    <div class="contact">
      <div class="contact__name">Dirk Malsworth</div>
      <div class="contact__title">President</div>
      <div class="contact__company">Solvane Holdings Inc.</div>
      <div class="contact__address">Street name, Suite 100<br>State, Zip Code, Country</div>
      <div class="contact__row">
        <svg viewBox="0 0 10 10" aria-hidden="true"><path d="M2 0.5 L3.6 2.6 L2.8 3.6 Q4 6 6.4 7.2 L7.4 6.4 L9.5 8 L8.4 9.5 Q4.5 9.4 1.6 6.4 Q0.5 4.5 0.6 1.6 Z"/></svg>
        555-239-7814
      </div>
      <div class="contact__row">
        <svg viewBox="0 0 10 10" aria-hidden="true"><path d="M0 2 H10 V8 H0 Z" /><path d="M0 2 L5 5.5 L10 2" fill="none" stroke="#fff" stroke-width="1"/></svg>
        dirk@solvaneholdings.example
      </div>
      <div class="contact__row">
        <svg viewBox="0 0 10 10" aria-hidden="true"><circle cx="5" cy="5" r="4.6"/><path d="M0.5 5 H9.5 M5 0.5 V9.5 M5 0.5 Q2 5 5 9.5 M5 0.5 Q8 5 5 9.5" fill="none" stroke="#fff" stroke-width="0.7"/></svg>
        solvaneholdings.example
      </div>
    </div>
  </section>
</body>
</html>
```